Handyman home maintenance postcard

We would like the postcard to state what we do : Painting, plumbing, electrical, flooring, carpentry, drywall, fencing, windows and more. We would also like our promotion to state : First four hours of work is only $299. Additional hours are 25% off our regular rate of $110 an hour. Rate includes two expert handymen working to complete your job.

Target Market(s)

30-75

Industry/Entity Type

Home maintenance

```html
<!DOCTYPE html>
<html lang="en">
<head>
<meta charset="utf-8">
<title>Steady Hand Services – Postcard</title>
<link href="https://fonts.googleapis.com/css2?family=Archivo+Black&family=Poppins:wght@400;500;600;700;800&display=swap" rel="stylesheet">
<style>
:root{
  --orange:#f7a21b;
  --orange-deep:#f08a12;
  --ink:#111111;
  --white:#ffffff;
  --page:#e4e4e4;
  --photo-warm:#c9b8a2;
  --photo-cool:#8fa9b3;
  --stamp:#e3e3e3;
}
*{box-sizing:border-box;margin:0;padding:0}
html,body{width:1200px;height:2655px;overflow:hidden;background:var(--page);font-family:"Poppins",sans-serif;color:var(--ink)}
.card{position:absolute;left:70px;width:1060px;height:680px;background:var(--white);overflow:hidden;box-shadow:0 10px 18px rgba(0,0,0,.28)}
.front{top:995px}
.back{top:1758px}

/* ---------- front ---------- */
.hero-photo{position:absolute;left:490px;top:0;width:570px;height:483px;
  background:linear-gradient(100deg,#f4efe9 0%,var(--photo-warm) 45%,var(--photo-cool) 100%);
  clip-path:polygon(0 0,100% 0,100% 100%,20% 100%,0 60%)}
.brand{position:absolute;display:flex;align-items:center;gap:10px;font-family:"Poppins",sans-serif;font-weight:700;color:var(--ink);white-space:nowrap}
.brand .dot{flex:none;border-radius:50%;background:var(--orange)}
.front .brand{left:45px;top:58px;font-size:30px}
.front .brand .dot{width:50px;height:50px}
.headline{position:absolute;left:46px;top:172px;font-family:"Archivo Black",sans-serif;line-height:1;text-transform:uppercase}
.headline .lead{display:block;color:var(--orange);font-size:53px;margin-bottom:9px}
.headline .rest{display:block;font-size:53px;margin-bottom:9px;letter-spacing:-.5px}
.tagline{position:absolute;left:47px;top:357px;font-size:25px;font-weight:600}
.offer-badge{position:absolute;border-radius:50%;background:var(--orange);border:5px solid var(--ink);display:flex;flex-direction:column;align-items:center;justify-content:center;text-align:center;font-weight:600;overflow:hidden}
.front .offer-badge{left:487px;top:105px;width:184px;height:184px}
.offer-badge .hours{background:var(--ink);color:var(--white);width:100%;font-weight:700}
.front .offer-badge .first{font-size:15px}
.front .offer-badge .hours{font-size:27px;line-height:1.15}
.front .offer-badge .only{font-size:14px;font-weight:700}
.offer-badge .price{font-family:"Archivo Black",sans-serif;line-height:1}
.front .offer-badge .price{font-size:50px}
.promo-band{position:absolute;left:0;top:402px;width:1060px;height:128px;background:var(--orange-deep);
  clip-path:polygon(0 0,550px 0,620px 81px,100% 81px,100% 100%,0 100%)}
.promo-line{position:absolute;left:48px;color:var(--white);font-weight:600;font-size:25px;display:flex;align-items:center;gap:14px;white-space:nowrap}
.pill{background:var(--ink);color:var(--white);border-radius:5px;padding:0 12px;font-weight:600}
.front .l1{top:407px}.front .l2{top:443px}.front .l3{top:483px}
.front .l3 .pill{font-size:23px}
.cta-band{position:absolute;left:0;bottom:0;background:var(--ink);color:var(--white)}
.front .cta-band{top:530px;width:1060px}
.cta-get{position:absolute;font-weight:600;line-height:1}
.cta-get .free{display:block;color:var(--orange);font-weight:800}
.front .cta-get{left:50px;top:20px;font-size:40px}
.front .cta-get .free{font-size:54px;margin-top:2px}
.call-box{position:absolute;border:2px solid var(--white);border-radius:6px;display:flex;align-items:center;gap:14px;font-weight:700;white-space:nowrap}
.call-box svg{flex:none}
.front .call-box{left:514px;top:15px;width:470px;height:53px;padding:0 14px;font-size:35px}
.web .accent{color:var(--orange)}
.front .web{position:absolute;left:514px;top:70px;font-size:27px;font-weight:600}

/* ---------- back ---------- */
.about{position:absolute;left:0;top:0;width:590px;height:190px;background:linear-gradient(90deg,#1c1916,#2b2620 60%,#1a1815);color:var(--white);padding:44px 20px 0 48px}
.about h2,.offer h2{font-size:24px;font-weight:800;line-height:1}
.about h2 .accent{color:var(--orange)}
.about p{font-size:12.4px;line-height:1.25;margin-top:6px}
.offer{position:absolute;left:0;top:190px;width:590px;height:332px;background:var(--orange)}
.offer h2{position:absolute;left:50px;top:22px;color:var(--ink);border-bottom:2px solid var(--ink);padding-bottom:2px;width:262px}
.offer h2 .accent{color:var(--white)}
.service-list{position:absolute;top:62px;list-style:none;font-size:17px;line-height:25px;color:var(--ink)}
.service-list li{display:flex;align-items:center;gap:7px}
.service-list li::before{content:"";width:11px;height:11px;border-radius:50%;background:var(--white)}
.col-a{left:52px}.col-b{left:188px}
.worker-photo{position:absolute;left:373px;top:37px;width:186px;height:150px;border:3px solid var(--white);background:linear-gradient(135deg,#a9bfc9,#5d7a8c)}
.back .offer-badge{left:338px;top:3px;width:100px;height:100px;border-width:4px;background:var(--ink);border-color:var(--white);z-index:1}
.back .offer-badge .first{font-size:8px;line-height:1.2;color:var(--white)}
.back .offer-badge .hours{font-size:13px;line-height:1.2;color:var(--orange);background:transparent}
.back .offer-badge .only{font-size:7px;line-height:1.3;color:var(--white)}
.back .offer-badge .price{font-size:25px;color:var(--orange);margin-top:1px}
.thumb{position:absolute;top:210px;width:166px;height:105px;border:3px solid var(--white)}
.t1{left:45px;background:linear-gradient(135deg,#8a8269,#3e3a2c)}
.t2{left:224px;background:linear-gradient(135deg,#d8d8d6,#9a9a98)}
.t3{left:403px;background:linear-gradient(135deg,#c5a48a,#5b6674)}
.back .cta-band{top:522px;width:612px;clip-path:polygon(0 0,590px 0,612px 22px,100% 100%,0 100%)}
.back .cta-get{left:48px;top:22px;font-size:18px}
.back .cta-get .free{font-size:22px}
.back .call-box{left:222px;top:22px;width:298px;height:34px;padding:0 8px;font-size:21px;gap:8px}
.contact{position:absolute;left:48px;font-size:18px;font-weight:500;display:flex;align-items:center;gap:8px}
.contact.mail{top:72px}.contact.site{top:96px}
.address-side .brand{left:622px;top:70px;font-size:17px;gap:7px}
.address-side .brand .dot{width:30px;height:30px}
.stamp{position:absolute;left:911px;top:52px;width:98px;height:98px;border-radius:6px;background:var(--stamp);border:2px solid #cfcfcf}
</style>
</head>
<body>

<section class="card front">
  <div class="hero-photo" role="img" aria-label="Photo of a smiling handyman in a cap and tool belt fixing a kitchen cabinet"></div>
  <div class="brand"><span class="dot"></span>Steady Hand Services</div>
  <h1 class="headline"><span class="lead">Trusted</span><span class="rest">Handyman &amp;</span><span class="rest">Repair Services</span></h1>
  <p class="tagline">Your Expert Go-To For Home Repairs</p>
  <div class="offer-badge"><span class="first">FIRST</span><span class="hours">4 HOURS</span><span class="only">OF WORK IS ONLY</span><span class="price">$299</span></div>
  <div class="promo-band"></div>
  <p class="promo-line l1">Additional hours are <span class="pill">25% OFF</span></p>
  <p class="promo-line l2">Our regular rate of <span class="pill">$110 AN HOUR</span></p>
  <p class="promo-line l3"><span class="pill">RATE INCLUDES</span> Two expert handymen working to complete your job</p>
  <div class="cta-band">
    <p class="cta-get">Get Your<span class="free">Free Estimate!</span></p>
    <div class="call-box">CALL US
      <svg width="34" height="34" viewBox="0 0 24 24" aria-hidden="true"><circle cx="12" cy="12" r="11" fill="none" stroke="#f7a21b" stroke-width="2"/><path d="M8.5 6.5l2 2-1.2 1.6a7 7 0 0 0 4.6 4.6l1.6-1.2 2 2-1.4 1.8c-4.6-.4-8.9-4.7-9.3-9.3z" fill="#f7a21b"/></svg>
      555 014 2368</div>
    <p class="web">www.<span class="accent">steadyhandservices</span>.com</p>
  </div>
</section>

<section class="card back">
  <div class="about">
    <h2>ABOUT <span class="accent">US</span></h2>
    <p>Steady Hand Services strives to be your go-to for home repairs. We have many years of experience in all facets of home repair and maintenance. Whether you are looking to repair that running toilet, replace that tired looking floor or give your home’s exterior or interior a fresh new color, we can get it done for you. On time, neatly and at a reasonable price.</p>
  </div>
  <div class="offer">
    <h2>WHAT <span class="accent">WE OFFER</span></h2>
    <ul class="service-list col-a"><li>Carpentry</li><li>Concrete</li><li>Drywall</li><li>Electrical</li><li>Fencing</li></ul>
    <ul class="service-list col-b"><li>Flooring</li><li>Maintenance</li><li>Painting</li><li>Picture Hanging</li><li>Plumbing</li></ul>
    <div class="worker-photo" role="img" aria-label="Photo of a plumber in a blue cap working on pipes"></div>
    <div class="offer-badge"><span class="first">FIRST</span><span class="hours">4 HOURS</span><span class="only">OF WORK IS ONLY</span><span class="price">$299</span></div>
    <div class="thumb t1" role="img" aria-label="Photo of a drill fitting a cabinet hinge"></div>
    <div class="thumb t2" role="img" aria-label="Photo of a wrench on a sink drain pipe"></div>
    <div class="thumb t3" role="img" aria-label="Photo of an electrician testing a breaker panel"></div>
  </div>
  <div class="cta-band">
    <p class="cta-get">Get Your<span class="free">Free Estimate!</span></p>
    <div class="call-box">CALL US
      <svg width="22" height="22" viewBox="0 0 24 24" aria-hidden="true"><circle cx="12" cy="12" r="11" fill="none" stroke="#f7a21b" stroke-width="2"/><path d="M8.5 6.5l2 2-1.2 1.6a7 7 0 0 0 4.6 4.6l1.6-1.2 2 2-1.4 1.8c-4.6-.4-8.9-4.7-9.3-9.3z" fill="#f7a21b"/></svg>
      555 014 2368</div>
    <p class="contact mail"><svg width="16" height="12" viewBox="0 0 16 12" aria-hidden="true"><rect width="16" height="12" fill="#f7a21b"/><path d="M0 0l8 6 8-6" fill="none" stroke="#111" stroke-width="1.5"/></svg>hello@steadyhandservices.com</p>
    <p class="contact site"><svg width="16" height="16" viewBox="0 0 16 16" aria-hidden="true"><circle cx="8" cy="8" r="7" fill="none" stroke="#f7a21b" stroke-width="1.6"/><ellipse cx="8" cy="8" rx="3" ry="7" fill="none" stroke="#f7a21b" stroke-width="1.2"/><path d="M1 8h14" stroke="#f7a21b" stroke-width="1.2"/></svg>www.steadyhandservices.com</p>
  </div>
  <div class="address-side">
    <div class="brand"><span class="dot"></span>Steady Hand Services</div>
    <div class="stamp"></div>
  </div>
</section>

</body>
</html>
```